BRSP Business Card Design Project

We are a Wedding Film company in Charleston, SC In need of a unique business card. Our website is www.brightspiralreels.example. Check us out to get an idea of who we are and what we do. The design should be upscale but not pretentious. Modern but not cheesy. I will most likely have our cards printed by Zib on the Opal design. I'm also liking the raised designs for our logo. The Wedding Films in our logo on our site is blue so feel free to manipulate our logo for your designs as well.

Industry/Entity Type

Business

Requirements
Must have
• This is the info I want on the card:

Derek Hollisbury
Storyteller

Brightspiral Wedding Reels
www.brightspiralreels.example

555.208.4417
derek@brightspiralreels.example

```html
<!DOCTYPE html>
<html lang="en">
<head>
<meta charset="utf-8">
<title>Brightspiral Wedding Reels – Business Card Options</title>
<link href="https://fonts.googleapis.com/css2?family=Source+Sans+3:wght@400;700&display=swap" rel="stylesheet">
<style>
  :root {
    --page: #ffffff;
    --ink: #000000;
    --paper: #ffffff;
    --night: #000000;
    --gold: #9b7f4a;
    --gold-light: #a8925f;
    --rule: #555555;
    --text-dark: #111111;
    --text-light: #ffffff;
    --leaf-light: #e9e3d6;
    --leaf-dark: #2a2622;
  }
  * { margin: 0; padding: 0; box-sizing: border-box; }
  html, body { width: 1200px; height: 798px; overflow: hidden; background: var(--page); }
  body { position: relative; font-family: "Source Sans 3", Arial, sans-serif; }

  .option-label {
    position: absolute; top: 74px; width: 504px; text-align: center;
    font-size: 50px; font-weight: 400; color: var(--ink); line-height: 1;
  }
  .option-label.first { left: 88px; }
  .option-label.second { left: 608px; }

  .card { position: absolute; width: 504px; height: 280px; overflow: hidden; }
  .card.light { background: var(--paper); border: 1px solid var(--rule); }
  .card.gold { background: var(--gold); border: 1px solid var(--rule); }
  .card.dark { background: var(--night); }
  .col-1 { left: 88px; }
  .col-2 { left: 608px; }
  .row-front { top: 146px; }
  .row-back { top: 432px; }

  .leaf-field {
    position: absolute; left: 200px; top: -40px; width: 360px; height: 360px; border-radius: 50%;
  }
  .light .leaf-field { background: radial-gradient(circle at 55% 50%, var(--leaf-light) 0%, var(--leaf-light) 45%, rgba(233,227,214,0) 72%); }
  .dark .leaf-field { background: radial-gradient(circle at 55% 50%, var(--leaf-dark) 0%, var(--leaf-dark) 45%, rgba(42,38,34,0) 72%); }

  .brand-mark { position: absolute; border-radius: 50%; background: var(--gold-light); }
  .front .brand-mark { left: 82px; top: 26px; width: 48px; height: 48px; }
  .brand-name {
    position: absolute; font-size: 16px; font-weight: 400; color: var(--gold-light);
    letter-spacing: 0.4px; white-space: nowrap; line-height: 1;
  }
  .front .brand-name { left: 14px; top: 96px; }

  .contact { position: absolute; left: 233px; top: 100px; font-size: 14.5px; line-height: 18.5px; }
  .light .contact { color: var(--text-dark); }
  .dark .contact { color: var(--text-light); }
  .contact .name { font-weight: 700; font-size: 16px; }
  .contact .gap { height: 20px; }

  .back-url { position: absolute; left: 0; width: 100%; text-align: center; font-size: 14.5px; }
  .gold .back-url { top: 131px; color: var(--text-light); }

  .back .brand-mark { left: 228px; top: 54px; width: 48px; height: 48px; }
  .back .brand-name { left: 0; width: 100%; text-align: center; top: 130px; font-size: 18px; }
  .band { position: absolute; left: 0; top: 223px; width: 100%; height: 30px; background: var(--gold); }
  .band .back-url { top: 6px; color: var(--text-dark); }
</style>
</head>
<body>
  <div class="option-label first">design 1</div>
  <div class="option-label second">design 2</div>

  <section class="card light front col-1 row-front">
    <div class="leaf-field" role="img" aria-label="Soft beige leaf pattern radiating across the card"></div>
    <div class="brand-mark"></div>
    <div class="brand-name">Brightspiral Wedding Reels</div>
    <div class="contact">
      <div class="name">Derek Hollisbury</div>
      <div>Storyteller</div>
      <div class="gap"></div>
      <div>Brightspiral Wedding Reels</div>
      <div>www.brightspiralreels.example</div>
      <div class="gap"></div>
      <div>555.208.4417</div>
      <div>derek@brightspiralreels.example</div>
    </div>
  </section>

  <section class="card gold col-1 row-back">
    <div class="back-url">www.brightspiralreels.example</div>
  </section>

  <section class="card dark front col-2 row-front">
    <div class="leaf-field" role="img" aria-label="Faint dark leaf pattern radiating across the card"></div>
    <div class="brand-mark"></div>
    <div class="brand-name">Brightspiral Wedding Reels</div>
    <div class="contact">
      <div class="name">Derek Hollisbury</div>
      <div>Storyteller</div>
      <div class="gap"></div>
      <div>Brightspiral Wedding Reels</div>
      <div>www.brightspiralreels.example</div>
      <div class="gap"></div>
      <div>555.208.4417</div>
      <div>derek@brightspiralreels.example</div>
    </div>
  </section>

  <section class="card dark back col-2 row-back">
    <div class="brand-mark"></div>
    <div class="brand-name">Brightspiral Wedding Reels</div>
    <div class="band"><div class="back-url">www.brightspiralreels.example</div></div>
  </section>
</body>
</html>
```